Newsletter for a recent surgical mission conducted by Bright Path Outreach

We need a one page, two sided newsletter reporting the events of our recent mission trip. The first page should have the title Bright Path Outreach along with the mission date of November 2019 and Cayo, Belize as the location. We want to highlight the pictures of the children especially the before and after pictures. Pictures of the hospital and ward should give the viewer the feel that they visited the hospital with us and to show how basic and rustic it is. Maybe stock photos of mountainous green landscape would help.

Target Market(s)

Our donors receive this and we want to highlight what we did and how their contributions enabled us to do it.

Industry/Entity Type

Non Profit

Font styles to use
Sans Serif

Colors

Designer to choose colors to be used in the design.

Requirements
Must have
• 1. The organization logo
• 2. Please match the text describing each patient to the corresponding pictures of the patients.
• 3. Highlighted text thanking our donors for donating.
• 4. www.brightpathoutreach should be included which is our website.
• 5. Text asking anyone who wants to contribute to our next mission to visit the Donate link on our website.
Nice to have
• 1. Stock images of the Belizean landscape can be used along with the picture of the hospital.
• 2. I am not sure what 'GREYSCALE" is but it might be interesting to see what a version of the newsletter looks like in that color. We have always matched the colors in the logo. If not, then just match the colors in the logo but let the designer choose.
Should not have
• When including the picture of us the surgeons, keep it small. We want to highlight the patients NOT the staff.

```html
<!DOCTYPE html>
<html lang="en">
<head>
<meta charset="utf-8">
<title>Bright Path Outreach — Mission Newsletter</title>
<link rel="stylesheet" href="https://fonts.googleapis.com/css2?family=Open+Sans:ital,wght@0,400;0,600;0,700;1,400;1,600;1,700&display=swap">
<style>
:root{
  --bg:#cbc7c8;
  --paper:#ffffff;
  --green:#8fb574;
  --green-dark:#6f9a55;
  --blue:#1f4f8c;
  --ink:#222222;
  --photo-sky:#a9c4dc;
  --photo-ground:#8da36a;
  --photo-scrubs:#5f8f7e;
  --photo-skin:#caa184;
  --photo-ward:#5f9a6a;
  --photo-room:#d4d8dc;
}
*{box-sizing:border-box;margin:0;padding:0}
html,body{width:1200px;height:1200px;overflow:hidden}
body{background:var(--bg);font-family:"Open Sans",Arial,sans-serif;color:var(--ink);position:relative}
.page{position:absolute;top:238px;width:560px;height:725px;background:var(--paper);overflow:hidden;box-shadow:0 6px 18px rgba(0,0,0,.18)}
.page--front{left:28px}
.page--back{left:612px}
.art{position:absolute;left:0;top:0}
.logo-name{position:absolute;text-align:center;font-family:"Open Sans",Arial,sans-serif;font-weight:700;color:var(--blue);font-size:14px;line-height:1.15;letter-spacing:.04em;text-transform:uppercase}
.body-text{position:absolute;font-size:10.2px;line-height:1.5;hyphens:auto;-webkit-hyphens:auto}
.body-text p+p{margin-top:10px}
.centered{text-align:center}
.dropcap{float:left;font-size:58px;line-height:.8;color:var(--green);font-weight:400;margin:3px 5px 0 0}
.lead-in{font-variant:small-caps;color:var(--green-dark);font-weight:600}
.bold-it{font-weight:700;font-style:italic}
.thanks{color:var(--green-dark);font-style:italic;font-weight:600;text-align:center;font-size:10.4px;line-height:1.55;padding:0 8px}
.site-line{position:absolute;left:0;right:0;bottom:25px;display:flex;align-items:center;justify-content:center;gap:10px;color:var(--blue);font-weight:700;font-size:11.5px;line-height:1;letter-spacing:.12em}
.site-line::before,.site-line::after{content:"";width:40px;height:1.5px;background:var(--blue)}
.footer-band{position:absolute;left:0;right:0;bottom:0;height:20px;background:var(--green)}
.top-strip{position:absolute;left:0;right:0;top:0;height:20px;background:var(--green)}
.gap-right{float:right;width:90px;height:215px}
.shape-left{float:left;width:112px;height:262px;shape-outside:polygon(0 0,78px 0,108px 80px,112px 140px,102px 205px,70px 240px,0 262px)}
.shape-right{float:right;width:127px;height:290px;shape-outside:polygon(6px 0,127px 0,127px 290px,40px 290px,36px 160px,0 150px)}
.donate-band{position:absolute;left:0;right:0;top:398px;height:54px;background:var(--green);display:flex;flex-direction:column;align-items:center;justify-content:center;text-align:center;font-weight:700;font-size:10.4px;letter-spacing:.12em;line-height:1.6;color:var(--paper);text-transform:uppercase}
.donate-band .hl{color:var(--blue)}
</style>
</head>
<body>

<section class="page page--front">
  <svg class="art" width="560" height="725" viewBox="0 0 560 725">
    <defs>
      <linearGradient id="sceneHospital" x1="0" y1="0" x2="0" y2="1">
        <stop offset="0" stop-color="var(--photo-sky)"/>
        <stop offset=".55" stop-color="#e8d6cf"/>
        <stop offset="1" stop-color="var(--photo-ground)"/>
      </linearGradient>
      <linearGradient id="sceneSurgery" x1="0" y1="0" x2="1" y2="1">
        <stop offset="0" stop-color="var(--photo-scrubs)"/>
        <stop offset="1" stop-color="#3f6b5e"/>
      </linearGradient>
      <linearGradient id="sceneChild" x1="0" y1="0" x2="1" y2="1">
        <stop offset="0" stop-color="var(--photo-skin)"/>
        <stop offset="1" stop-color="#e9dfd8"/>
      </linearGradient>
      <linearGradient id="sceneWard" x1="0" y1="0" x2="1" y2="1">
        <stop offset="0" stop-color="#7d93c4"/>
        <stop offset="1" stop-color="#e6e2dc"/>
      </linearGradient>
    </defs>
    <path role="img" aria-label="Photo of the community hospital building with ambulances parked outside" d="M0 0 H560 V190 C480 255 380 290 270 282 C190 268 110 180 0 128 Z" fill="url(#sceneHospital)"/>
    <path role="img" aria-label="Photo of the surgical team operating" d="M0 128 C110 180 190 268 270 282 C200 305 120 312 0 296 Z" fill="url(#sceneSurgery)"/>
    <path d="M0 128 C110 180 190 268 270 282" fill="none" stroke="var(--green)" stroke-width="7"/>
    <path d="M270 298 C370 298 470 258 560 195" fill="none" stroke="var(--green)" stroke-width="7"/>
    <circle cx="262" cy="232" r="64" fill="var(--paper)" stroke="var(--green)" stroke-width="4"/>
    <circle role="img" aria-label="Photo of a patient and surgeon in the ward" cx="512" cy="440" r="56" fill="url(#sceneWard)" stroke="var(--green)" stroke-width="4"/>
    <circle role="img" aria-label="Photo of the patient's bandaged arm after surgery" cx="522" cy="558" r="56" fill="url(#sceneChild)" stroke="var(--green)" stroke-width="4"/>
    <circle role="img" aria-label="Before photo of infant patient with cleft lip" cx="50" cy="596" r="44" fill="url(#sceneChild)" stroke="var(--green)" stroke-width="4"/>
    <circle role="img" aria-label="After photo of infant patient following lip repair" cx="116" cy="636" r="52" fill="url(#sceneChild)" stroke="var(--green)" stroke-width="4"/>
  </svg>
  <div class="logo-name" style="left:200px;top:216px;width:124px">Bright Path<br>Outreach</div>

  <div class="body-text" style="left:36px;top:330px;width:258px">
    <p><span class="dropcap">T</span><span class="lead-in">he Bright Path Outreach Team returned</span> to the Cayo District of Belize for a weeklong mission working with the staffs of the <span class="bold-it">Riverside Community Hospital and the Valley Regional Medical Center</span> in Belmopan. The Team performed primarily cleft lip and palate surgery which is not readily available to children in need throughout the country.</p>
    <p class="thanks" style="margin-top:14px">Many thanks to all those who donated in support of our mission, enabling us to provide life changing surgery and positively impact so many lives.</p>
  </div>

  <div class="body-text centered" style="left:184px;top:550px;width:124px">
    <p>This is Lena Marsh from the small town of Spanish Lookout in Cayo, Belize. Lena is five months old and was born with a cleft lip</p>
  </div>

  <div class="body-text" style="left:318px;top:326px;width:224px">
    <p>and palate. The Team was able to help her by performing the first of four surgeries she will need to reconstruct her lip, palate and nose.</p>
  </div>
  <div class="body-text" style="left:318px;top:394px;width:224px">
    <div class="gap-right"></div>
    <p>This is Rafael Ortega, a 23 year old man from the town of Santa Elena in Cayo. He sustained a left upper arm injury from a rotating saw four years ago that lacerated his radial nerve. It was never repaired and now he cannot extend his wrist, thumb and fingers. The Team performed forearm muscle and tendon transfers which after a six-week recovery will allow him to get back to work doing construction.</p>
  </div>

  <div class="site-line">WWW.BRIGHTPATHOUTREACH.COM</div>
  <div class="footer-band"></div>
</section>

<section class="page page--back">
  <div class="top-strip"></div>
  <svg class="art" width="560" height="725" viewBox="0 0 560 725">
    <defs>
      <linearGradient id="sceneKid" x1="0" y1="0" x2="1" y2="1">
        <stop offset="0" stop-color="var(--photo-skin)"/>
        <stop offset="1" stop-color="#efe6df"/>
      </linearGradient>
      <linearGradient id="sceneWardRoom" x1="0" y1="0" x2="1" y2="1">
        <stop offset="0" stop-color="var(--photo-ward)"/>
        <stop offset=".6" stop-color="#3c6aa0"/>
        <stop offset="1" stop-color="#9b5a3a"/>
      </linearGradient>
      <linearGradient id="sceneStaff" x1="0" y1="0" x2="1" y2="1">
        <stop offset="0" stop-color="var(--photo-room)"/>
        <stop offset="1" stop-color="#2f5f98"/>
      </linearGradient>
    </defs>
    <circle role="img" aria-label="Before photo of infant patient with severe cleft lip" cx="46" cy="48" r="60" fill="url(#sceneKid)" stroke="var(--green)" stroke-width="4"/>
    <circle role="img" aria-label="Photo of mother holding her infant after lip repair" cx="70" cy="168" r="72" fill="url(#sceneKid)" stroke="var(--green)" stroke-width="4"/>
    <circle role="img" aria-label="Photo of the young patient with his mother and father" cx="490" cy="112" r="86" fill="url(#sceneKid)" stroke="var(--green)" stroke-width="4"/>
    <circle role="img" aria-label="Photo of the young patient in a surgical cap" cx="506" cy="250" r="66" fill="url(#sceneKid)" stroke="var(--green)" stroke-width="4"/>

    <path role="img" aria-label="Photo of the children's ward with a painted mural and families" d="M0 505 C90 472 190 465 290 482 L290 725 H0 Z" fill="url(#sceneWardRoom)"/>
    <path role="img" aria-label="Photo of the surgeons standing together" d="M372 522 C440 502 500 492 560 496 V712 C510 690 450 662 372 642 Z" fill="url(#sceneStaff)"/>
    <path d="M0 505 C90 472 190 465 290 482" fill="none" stroke="var(--green)" stroke-width="7"/>
    <path d="M372 522 C440 502 500 492 560 496" fill="none" stroke="var(--green)" stroke-width="7"/>
    <path d="M372 642 C450 662 510 690 560 712" fill="none" stroke="var(--green)" stroke-width="7"/>
    <circle cx="324" cy="558" r="72" fill="var(--paper)" stroke="var(--green)" stroke-width="4"/>
  </svg>
  <div class="logo-name" style="left:260px;top:542px;width:128px">Bright Path<br>Outreach</div>

  <div class="body-text" style="left:30px;top:32px;width:246px">
    <div class="shape-left"></div>
    <p class="centered">This is Mateo Cruz and his mother, Rosa. Mateo is seven months old and was born with a severe cleft lip. His mom brought him to see us and the Team was able to repair his cleft lip this week before they head back to their home in Stann Creek, Cayo.</p>
    <p>The Valley Regional Medical Center in Belmopan is the secondary receiving center for all of the smaller community hospitals and clinics throughout all of the Cayo District. It maintains a large clinic system, Emergency Room, two operating rooms, and an adult, maternity, and pediatric ward totaling 40 beds. The BPO Team was fortunate to partner with</p>
  </div>
  <div class="body-text" style="left:285px;top:32px;width:240px">
    <div class="shape-right"></div>
    <p>the doctors and staff there doing our work.</p>
    <p>This is 5 year old Tomas Reyes with his Mom and Dad. They are from the Frank's Eddy Village in Belize. Tomas had his cleft lip and palate repaired when he was younger. Unfortunately, he developed an opening in the roof of his mouth afterwards (palatal fistula) that results in liquid and food in his mouth coming out his nose when he ate. The Team was able to repair his palate this week and in a short time get back to eating normally.</p>
  </div>

  <div class="donate-band">
    <span><span class="hl">If you would like to contribute</span> to our next mission, please visit the</span>
    <span><span class="hl">donate link</span> on our website <span class="hl">www.brightpathoutreach.com</span></span>
  </div>
</section>

</body>
</html>
```